Health Benefits Association Website Design

The Unified Household Wellspring Alliance (UHWA) is an organization formed for the purpose of providing its members better value for selected health benefits and services. Members can use the association benefits either in conjunction with or independently of other medical insurance they may have. Some of the benefits available include discounted dental and vision care and prescription mail order services. There is no limitation on who can join. This membership will be primarily marketed as a way to enhance the value of a fixed benefit health insurance plan although members do not have to have the insurance plan join the association.

We are seeking a design for a website to be used for consumers to get information about membership and for current members to be able to access their benefits. The website should include:

1) A landing page to provide a description of the UHWA

2) A secondary page that can be duplicated that will:
a. Provide a list of benefits
b. Provide a membership enrollment form
c. Provide a member’s only access page
d. Provide a contact page for more information

We are seeking a modern but conservative design that will reflect value, simplicity and good health. The site design will also need to be compatible for use with mobile phones and tablets.

A copy of the association logo is included with the submission. It will also need to be incorporated into the website design. Layouts of similar association websites have also been included for reference.

Target Market(s)

Ages 25 to 65 unmarried, married with no children, professionals, self-employed, active and healthy

Industry/Entity Type

Health And Wellness

Number of Pages Required

2 page

Font styles to use
Sans Serif

Colors

Designer to choose colors to be used in the design.

Requirements
Must have
• UHWA Logo (attached). Use colors from the logo in the website design.
Nice to have
• Graphics, if used, should convey health and fitness and skew toward a diverse array of adults 25 to 40.

```html
<!DOCTYPE html>
<html lang="en">
<head>
<meta charset="utf-8">
<title>UHWA — Health Benefits &amp; Services</title>
<link href="https://fonts.googleapis.com/css2?family=Open+Sans:wght@400;600;700&family=Merriweather+Sans:wght@800&display=swap" rel="stylesheet">
<style>
:root{
  --olive:#8e9a4b;
  --olive-dark:#7d8940;
  --yellow:#fdc800;
  --ink:#333;
  --muted:#777;
  --line:#e5e5e5;
  --page:#f7f7f7;
  --white:#fff;
}
*{box-sizing:border-box;margin:0;padding:0}
html,body{width:773px;height:1200px;overflow:hidden;background:var(--white)}
body{position:relative;font-family:"Open Sans",sans-serif;color:var(--ink)}
.abs{position:absolute}

/* header */
.header{left:0;top:0;width:773px;height:72px;background:var(--white)}
.brand{left:84px;top:0;width:106px;height:106px;border-radius:50%;background:var(--white);z-index:3;display:flex;align-items:center;justify-content:center;text-align:center;padding:0 12px}
.brand span{font-size:10px;font-weight:700;color:var(--olive);line-height:1.25;text-transform:uppercase}
.contact-bar{top:14px;right:85px;display:flex;gap:16px;font-size:7px;color:var(--muted);align-items:center}
.contact-bar b{color:var(--ink);font-size:8px;font-weight:600}
.cb-item{display:flex;align-items:center;gap:6px}
.cb-icon{width:20px;height:20px;border-radius:50%;background:var(--yellow);display:flex;align-items:center;justify-content:center}
.nav{top:48px;left:240px;display:flex;gap:25px;font-size:6.5px;text-transform:uppercase;color:var(--ink);align-items:center}
.nav .active{color:var(--olive);border-top:1.5px solid var(--olive);padding-top:3px;margin-top:-4px}

/* hero */
.hero{left:0;top:72px;width:773px;height:324px;background:linear-gradient(90deg,#f6edd6 0%,#efe0b8 40%,#c9a870 65%,#b99a5d 100%)}
.hero-photo{left:330px;top:72px;width:443px;height:324px;background:radial-gradient(ellipse at 55% 45%,#e2c6a2 0%,#c8a678 45%,rgba(190,160,100,0) 80%)}
.hero-title{left:84px;top:177px;font-family:"Merriweather Sans",sans-serif;font-weight:800;font-size:20px;line-height:24px;color:#1d1d1d;letter-spacing:.3px;white-space:nowrap}
.hero-text{left:85px;top:207px;width:300px;font-size:10.5px;line-height:20px;color:#333}
.btn{background:var(--yellow);color:var(--white);font-size:6px;font-weight:700;text-transform:uppercase;display:flex;align-items:center;justify-content:center;width:79px;height:27px}
.hero-btn{left:85px;top:259px}
.arrows{left:84px;top:330px}

/* welcome */
.welcome{left:0;top:396px;width:773px;height:146px;background:var(--olive);color:var(--white);text-align:center}
.welcome h2{margin-top:26px;font-size:15px;font-weight:700;letter-spacing:.3px}
.welcome p{font-size:6.3px;line-height:14.5px;width:580px;margin:6px auto 0}
.welcome p+p{margin-top:8px}
.notch{left:376px;top:541px}

/* cards */
.cards-band{left:0;top:542px;width:773px;height:270px;background:var(--page)}
.card{top:580px;width:139px;height:193px;background:var(--white);box-shadow:0 0 3px rgba(0,0,0,.15);text-align:center}
.card h3{font-size:7.3px;font-weight:700;color:var(--olive-dark);text-transform:uppercase;padding-top:11px;height:29px}
.card .photo{height:101px}
.card p{font-size:6.2px;line-height:13px;color:var(--muted);margin-top:6px}
.card a{display:block;font-size:5.8px;font-weight:700;color:var(--yellow);margin-top:5px;text-decoration:none}

/* about */
.about{left:0;top:812px;width:773px;height:236px;background:var(--olive);overflow:hidden}
.about-photo{left:380px;top:0;width:393px;height:236px;background:linear-gradient(135deg,#7fa85a 0%,#a7c07b 35%,#9fbfd8 60%,#cfd6dc 100%)}
.about-arc{left:0;top:0}
.about .kicker{left:85px;top:31px;font-size:10px;color:var(--white)}
.about h2{left:85px;top:45px;font-size:15px;font-weight:700;color:var(--white);letter-spacing:.3px}
.about .body{left:85px;top:78px;width:325px;font-size:6.3px;line-height:13.3px;color:var(--white)}
.about .body p+p{margin-top:8px}
.about .btn{left:85px;top:177px}

/* footer */
.f-title{top:1068px;font-size:10px;color:var(--ink)}
.f-text{top:1090px;font-size:7px;line-height:13px;color:var(--muted)}
.news-input{left:325px;top:1088px;width:138px;height:24px;border:1px solid #d8d8d8;font-size:7px;color:var(--muted);padding:7px 8px}
.news-btn{left:468px;top:1088px;width:54px;height:24px;font-size:6.5px}
.socials{left:582px;top:1090px;display:flex;gap:3px}
.socials span{width:24px;height:24px;border:1.2px solid #555;border-radius:50%}
.rule{left:0;top:1137px;width:773px;height:1px;background:var(--line)}
.f-nav{left:0;top:1156px;width:773px;text-align:center;font-size:6.5px;color:var(--muted);text-transform:uppercase}
.f-nav i{font-style:normal;margin:0 6px}
.copy{left:0;top:1172px;width:773px;text-align:center;font-size:6px;color:var(--muted);text-transform:uppercase}
</style>
</head>
<body>

<header class="abs header"></header>
<div class="abs brand"><span>Unified Household Wellspring Alliance</span></div>

<div class="abs contact-bar">
  <div class="cb-item">
    <div class="cb-icon"><svg width="9" height="9" viewBox="0 0 24 24"><path fill="#fff" d="M6.6 10.8a15 15 0 006.6 6.6l2.2-2.2c.3-.3.7-.4 1-.2 1.1.4 2.3.6 3.6.6.6 0 1 .4 1 1V20c0 .6-.4 1-1 1A17 17 0 013 4c0-.6.4-1 1-1h3.5c.6 0 1 .4 1 1 0 1.3.2 2.5.6 3.6.1.3 0 .7-.2 1z"/></svg></div>
    <span>Phone : <b>(+345) 210-4486</b></span>
  </div>
  <div class="cb-item">
    <div class="cb-icon"><svg width="9" height="9" viewBox="0 0 24 24"><path fill="#fff" d="M2 5h20v14H2z"/><path d="M2 5l10 8 10-8" stroke="#fdc800" stroke-width="2" fill="none"/></svg></div>
    <span>Email : <b>info@uhwalliance.org</b></span>
  </div>
</div>

<nav class="abs nav">
  <span class="active">Home</span><span>Benefits</span><span>News</span><span>Charities</span><span>Membership</span><span>Enroll</span><span>Members Area</span><span>Contact</span>
  <svg width="10" height="10" viewBox="0 0 12 12"><circle cx="5" cy="5" r="4" fill="none" stroke="#555" stroke-width="1"/><path d="M8 8l3 3" stroke="#555" stroke-width="1"/></svg>
</nav>

<section class="abs hero"></section>
<div class="abs hero-photo" role="img" aria-label="Smiling older couple embracing outdoors in autumn light"></div>
<h1 class="abs hero-title">HEALTH BENEFITS &amp; SERVICES</h1>
<p class="abs hero-text">Adipiscing elit, sed do eiusmod tempor incididunt ut labore et dolore magna aliqua. Ut enim ad minim...</p>
<div class="abs btn hero-btn">Learn more info</div>
<svg class="abs arrows" width="32" height="28" viewBox="0 0 32 28"><path d="M9 2L2 14l7 12M23 2l7 12-7 12" fill="none" stroke="#666" stroke-width="1"/></svg>

<section class="abs welcome">
  <h2>WELCOME TO UHWA</h2>
  <p>Welcome to the Unified Household Wellspring Alliance (UHWA). UHWA was started to be part of a senior-focused charitable organization that is different from other organizations with a similar perspective or mission. UHWA believes a charity should focus on raising money to support its mission, not its leaders. So, none of the UHWA officers or board members receive any compensation.</p>
  <p>Please read the description of what UHWA is about and how we go about raising money to support our mission.</p>
</section>
<div class="cards-band abs"></div>
<svg class="abs notch" width="20" height="10" viewBox="0 0 20 10"><path d="M0 0h20L10 10z" fill="#8e9a4b"/></svg>

<article class="abs card" style="left:85px">
  <h3>Tempor incididunt</h3>
  <div class="photo" role="img" aria-label="Doctors and nurse reviewing a chart in a hospital corridor" style="background:linear-gradient(135deg,#e8ecef,#9fb6c8)"></div>
  <p>Lorem ipsum dolor sit consectetur<br>adipiscing elit eiusmod...</p>
  <a>LEARN MORE INFO &gt;&gt;</a>
</article>
<article class="abs card" style="left:240px">
  <h3>Tempor incididunt</h3>
  <div class="photo" role="img" aria-label="Young family playing together in a sunny field" style="background:linear-gradient(180deg,#5a9bd8 0%,#a9cdea 55%,#8fa84a 100%)"></div>
  <p>Lorem ipsum dolor sit consectetur<br>adipiscing elit eiusmod...</p>
  <a>LEARN MORE INFO &gt;&gt;</a>
</article>
<article class="abs card" style="left:394px">
  <h3>Tempor incididunt</h3>
  <div class="photo" role="img" aria-label="Doctor consulting with an older patient" style="background:linear-gradient(90deg,#f1f1ef 0%,#d9d6d0 55%,#6b3a52 100%)"></div>
  <p>Lorem ipsum dolor sit consectetur<br>adipiscing elit eiusmod...</p>
  <a>LEARN MORE INFO &gt;&gt;</a>
</article>
<article class="abs card" style="left:549px">
  <h3>Tempor incididunt</h3>
  <div class="photo" role="img" aria-label="Older couple relaxing on a sofa at home" style="background:linear-gradient(135deg,#b8c89a,#e6e2d8 60%,#d0c8b8)"></div>
  <p>Lorem ipsum dolor sit consectetur<br>adipiscing elit eiusmod...</p>
  <a>LEARN MORE INFO &gt;&gt;</a>
</article>

<section class="abs about">
  <div class="abs about-photo" role="img" aria-label="Active older couple resting on a park bench beside a bicycle"></div>
  <svg class="abs about-arc" width="773" height="236" viewBox="0 0 773 236"><path d="M0 0h380q90 80 75 236H0z" fill="#8e9a4b"/><path d="M380 0q90 80 75 236" fill="none" stroke="#fff" stroke-width="3"/></svg>
  <div class="abs kicker">THE UNIFIED HOUSEHOLD</div>
  <h2 class="abs">WELLSPRING ALLIANCE</h2>
  <div class="abs body">
    <p>The Unified Household Wellspring Alliance (UHWA) is a non-for-profit philanthropic organization whose primary mission is to fund medical research programs affecting the over age 65 senior population. Its secondary mission is to disseminate senior-related information, including legislative summaries, lifestyle and financial information.</p>
    <p>UHWA leverages the collective buying power of its members to develop, create and distribute benefits, services, privileges and discounts for those members, including for healthcare, travel and consumer.</p>
  </div>
  <div class="abs btn">Learn more info</div>
</section>

<div class="abs f-title" style="left:85px">CONTACT US</div>
<div class="abs f-text" style="left:85px"># lorem ipsum Dummy<br>Text mcg lorem</div>
<div class="abs f-text" style="left:202px">(000)-121-1231<br>info@uhwalliance.org</div>
<div class="abs f-title" style="left:325px">NEWSLETTER</div>
<div class="abs news-input">Email:</div>
<div class="abs btn news-btn">Subscribe</div>
<div class="abs f-title" style="left:585px">FOLLOW US</div>
<div class="abs socials"><span></span><span></span><span></span><span></span></div>

<div class="abs rule"></div>
<div class="abs f-nav">Home<i>|</i>Benefits<i>|</i>News<i>|</i>Charities<i>|</i>Membership<i>|</i>Enroll<i>|</i>Members Area<i>|</i>Contact</div>
<div class="abs copy">Copyright © 2017 UHWA | All rights are reserved</div>

</body>
</html>
```